Design a styled business card for an intimacy and attachment psychologist

I am a Psychologist providing online therapy to patients across the United States. My work is interpersonal and emotion-focused, with an emphasis on the client-therapist relationship. My primary areas of work are very personal, including sexuality and gender, abuse and trauma, and grief and loss. My target audience will be adults of all ages 18+.
My business card should convey a warm and inviting feeling of professionalism that is also casual and comfortable.
The front should be fairly simple and professional, consisting of:
- My name, Dr. Rosalind Petrakis
- My title, Licensed Psycholigist
- My logo
On either the front or the back, my contact information should be listed:
- ros@drrospetrakis.example
- 555.014.7788
- drrospetrakis.example
On the rear, I would like a description of the areas that I specialize in. This can be formatted in any way that appears stylistically interesting.
Individual and Couples
Relationships and Infidelity
Sexual Health & Aging
Gender Identity & Sexual Orientation
Abuse and Trauma
Sexual Compulsivity & Addiction
Sexual Dysfunction
Target Market(s)
My target audience will be adults of all ages 18+.
Industry/Entity Type
Psychology
Contact Information for Business Card
The front should be fairly simple and professional, consisting of: - My name, Dr. Rosalind Petrakis - My title, Licensed Psycholigist - My logo On either the front or the back, my contact information should be listed: - ros@drrospetrakis.example - 555.014.7788 - drrospetrakis.example On the rear, I would like a description of the areas that I specialize in. This can be formatted in any way that appears stylistically interesting. Individual and Couples Relationships and Infidelity Sexual Health & Aging Gender Identity & Sexual Orientation Abuse and Trauma Sexual Compulsivity & Addiction Sexual Dysfunction
- Follow brand guide

```html
<!DOCTYPE html>
<html lang="en">
<head>
<meta charset="utf-8">
<title>Dr. Rosalind Petrakis – Business Card</title>
<link rel="stylesheet" href="https://fonts.googleapis.com/css2?family=Montserrat:wght@400;500;600;700&display=swap">
<style>
  :root{
    --page:#d9d9dc;
    --ink:#2d2850;
    --ink-soft:#4a4a55;
    --plum-light:#6c6585;
    --plum-dark:#2b2550;
    --paper:#f2f2f3;
    --white:#ffffff;
    --accent:#e8474c;
    --mark:#6fc2b0;
  }
  *{box-sizing:border-box;margin:0;padding:0}
  html,body{width:1200px;height:1200px;overflow:hidden}
  body{
    background:var(--page);
    font-family:"Montserrat",Arial,sans-serif;
    display:flex;flex-direction:column;align-items:center;justify-content:center;gap:60px;
  }
  .card{
    width:900px;height:514px;border-radius:28px;position:relative;overflow:hidden;
    box-shadow:0 10px 24px rgba(0,0,0,.18);
  }
  /* back */
  .card--back{
    background:linear-gradient(100deg,var(--plum-light) 0%,var(--plum-dark) 58%);
    color:var(--white);
  }
  .brand{display:flex;align-items:center;gap:22px}
  .brand__dot{width:96px;height:96px;border-radius:50%;background:var(--mark);flex:none}
  .brand__name{font-weight:600;font-size:40px;letter-spacing:.04em;line-height:1.05;text-transform:uppercase}
  .card--back .brand{position:absolute;left:230px;top:56px}
  .pill{
    position:absolute;left:50%;top:228px;transform:translateX(-50%);
    background:var(--white);color:var(--plum-dark);font-weight:700;font-size:22px;
    padding:10px 34px;border-radius:30px;white-space:nowrap;
  }
  .specialties{list-style:none;font-size:18px;line-height:1.55;letter-spacing:.02em}
  .specialties li{display:flex;align-items:center;gap:10px}
  .specialties li::before{content:"";width:8px;height:8px;border-radius:50%;background:var(--accent);flex:none}
  .specialties--left{position:absolute;left:56px;bottom:48px}
  .specialties--right{position:absolute;right:56px;top:320px;text-align:right}
  .specialties--right li{flex-direction:row-reverse}
  /* front */
  .card--front{background:var(--paper);color:var(--ink)}
  .card--front .brand{position:absolute;right:64px;top:46px;color:var(--ink)}
  .card--front .brand__dot{width:84px;height:84px}
  .card--front .brand__name{font-size:34px}
  .identity{position:absolute;left:64px;top:250px;right:64px}
  .identity__name{font-weight:700;font-size:30px}
  .identity__title{font-size:19px;color:var(--ink-soft);margin-top:4px}
  .rule{height:2px;background:var(--ink);margin:16px 0 14px}
  .contact{font-size:18px;color:var(--ink-soft);line-height:1.7}
  .contact__row{display:flex;align-items:center;gap:12px}
  .contact__row svg{width:18px;height:18px;flex:none}
  .contact--email{position:absolute;right:64px;top:380px}
</style>
</head>
<body>
  <section class="card card--back" aria-label="Card back: specialties">
    <div class="brand">
      <span class="brand__dot"></span>
      <span class="brand__name">Dr. Rosalind<br>Petrakis</span>
    </div>
    <div class="pill">I am Specialize in</div>
    <ul class="specialties specialties--left">
      <li>Individual and Couples</li>
      <li>Relationships and Infidelity</li>
      <li>Sexual Compulsivity &amp; Addiction</li>
      <li>Gender Identity &amp; Sexual Orientation</li>
    </ul>
    <ul class="specialties specialties--right">
      <li>Sexual Health &amp; Aging</li>
      <li>Sexual Dysfunction</li>
      <li>Sexual Dysfunction</li>
    </ul>
  </section>

  <section class="card card--front" aria-label="Card front: contact">
    <div class="brand">
      <span class="brand__dot"></span>
      <span class="brand__name">Dr. Rosalind<br>Petrakis</span>
    </div>
    <div class="identity">
      <p class="identity__name">Dr. Rosalind Petrakis</p>
      <p class="identity__title">Licensed Psycholigist</p>
      <div class="rule"></div>
      <div class="contact">
        <p>4410 Alder Lane Brookfield Maine 04090</p>
        <p class="contact__row">
          <svg viewBox="0 0 24 24" aria-hidden="true"><path fill="var(--ink)" d="M6.6 10.8a15 15 0 0 0 6.6 6.6l2.2-2.2a1 1 0 0 1 1-.25 11.4 11.4 0 0 0 3.6.57 1 1 0 0 1 1 1V20a1 1 0 0 1-1 1A17 17 0 0 1 3 4a1 1 0 0 1 1-1h3.5a1 1 0 0 1 1 1c0 1.25.2 2.45.57 3.6a1 1 0 0 1-.25 1z"/></svg>
          555.014.7788
        </p>
        <p class="contact__row">
          <svg viewBox="0 0 24 24" aria-hidden="true"><circle cx="12" cy="12" r="9" fill="none" stroke="var(--ink)" stroke-width="2"/><path d="M3 12h18M12 3c3 3 3 15 0 18M12 3c-3 3-3 15 0 18" fill="none" stroke="var(--ink)" stroke-width="1.6"/></svg>
          www.drrospetrakis.example
        </p>
      </div>
    </div>
    <p class="contact contact--email contact__row">
      <svg viewBox="0 0 24 24" aria-hidden="true"><rect x="2" y="5" width="20" height="14" rx="1.5" fill="var(--ink)"/><path d="M3 6l9 7 9-7" fill="none" stroke="var(--paper)" stroke-width="1.8"/></svg>
      ros@drrospetrakis.example
    </p>
  </section>
</body>
</html>
```